Painting Contractor Business Card Design

We are looking for a cool, bold, modern, polished, business card design. We are a high-end residential painting contractor. Please incorporate our logo and keep with our green/black color scheme. We are interested in seeing 2-sided and 1-sided options. Thank you very much!

Industry/Entity Type

Business

Contact Information for Business Card

Info for the card:
Dale Ormsby
mobile 206-555-0193
email dale@tallowbrookpainting.net
web www.tallowbrookpainting.net

```html
<!DOCTYPE html>
<html lang="en">
<head>
<meta charset="utf-8">
<title>Tallowbrook Painting – Business Card</title>
<link rel="stylesheet" href="https://fonts.googleapis.com/css2?family=Roboto:wght@400;500&display=swap">
<style>
  :root {
    --page-bg: #ecebe8;
    --card-bg: #fbfbfb;
    --card-edge: #e4e4e4;
    --ink: #3a3a3a;
    --ink-soft: #5a5a5a;
    --rule: #c9c9c9;
    --brand-green: #8cc152;
    --brand-yellow: #e8b82e;
    --brand-red: #c0392b;
    --wordmark: #4a4a4a;
  }
  * { margin: 0; padding: 0; box-sizing: border-box; }
  html, body { width: 1200px; height: 780px; overflow: hidden; }
  body {
    background: var(--page-bg);
    font-family: "Roboto", Arial, sans-serif;
    color: var(--ink);
    display: flex;
    align-items: center;
    justify-content: center;
    gap: 60px;
  }
  .card {
    position: relative;
    width: 520px;
    height: 300px;
    background: linear-gradient(160deg, #ffffff 0%, var(--card-bg) 55%, #efefef 100%);
    border-radius: 16px;
    overflow: hidden;
    box-shadow: 0 1px 0 var(--card-edge), 0 10px 26px rgba(0,0,0,0.12);
  }

  /* Front side */
  .card-front .logo-block {
    position: absolute;
    left: 24px; top: 0;
    width: 206px; height: 256px;
    display: flex;
    flex-direction: column;
    align-items: center;
    justify-content: center;
    gap: 14px;
  }
  .brand-square {
    width: 16px; height: 16px;
    background: var(--brand-green);
    flex: none;
  }
  .card-front .brand-square { width: 22px; height: 22px; }
  .wordmark {
    font-weight: 500;
    color: var(--wordmark);
    text-transform: uppercase;
    white-space: nowrap;
  }
  .card-front .wordmark { font-size: 14px; letter-spacing: 0.6px; }
  .card-front .divider {
    position: absolute;
    left: 250px; top: 60px;
    width: 1px; height: 140px;
    background: var(--rule);
  }
  .contact-block {
    position: absolute;
    left: 282px; top: 58px;
  }
  .person-name {
    font-size: 22px;
    font-weight: 500;
    letter-spacing: 0.5px;
    text-transform: uppercase;
    color: var(--ink);
    margin-bottom: 30px;
  }
  .contact-list { list-style: none; }
  .contact-item {
    display: flex;
    align-items: center;
    gap: 9px;
    font-size: 12.5px;
    color: var(--ink-soft);
    margin-bottom: 9px;
    white-space: nowrap;
  }
  .contact-icon {
    width: 17px; height: 17px;
    border-radius: 4px;
    display: flex;
    align-items: center;
    justify-content: center;
    flex: none;
  }
  .contact-icon svg { width: 11px; height: 11px; }
  .icon-phone { background: var(--brand-green); }
  .icon-mail { background: var(--brand-yellow); }
  .icon-web { background: var(--brand-red); }

  .color-band {
    position: absolute;
    left: 0; bottom: 0;
    width: 100%; height: 44px;
    display: flex;
  }
  .band-green { flex: 42; background: var(--brand-green); }
  .band-yellow { flex: 33; background: var(--brand-yellow); }
  .band-red { flex: 25; background: var(--brand-red); }

  /* Back side */
  .card-back {
    display: flex;
    align-items: center;
    justify-content: center;
    gap: 14px;
  }
  .card-back .brand-square { width: 24px; height: 24px; }
  .card-back .wordmark { font-size: 30px; letter-spacing: 1.5px; }
</style>
</head>
<body>

  <section class="card card-front" aria-label="Business card front">
    <div class="logo-block">
      <span class="brand-square"></span>
      <span class="wordmark">Tallowbrook Painting</span>
    </div>
    <div class="divider"></div>
    <div class="contact-block">
      <h1 class="person-name">Dale Ormsby</h1>
      <ul class="contact-list">
        <li class="contact-item">
          <span class="contact-icon icon-phone">
            <svg viewBox="0 0 12 12"><rect x="3" y="1" width="6" height="10" rx="1" fill="none" stroke="#fff" stroke-width="1.3"/><circle cx="6" cy="9" r="0.7" fill="#fff"/></svg>
          </span>
          206-555-0193
        </li>
        <li class="contact-item">
          <span class="contact-icon icon-mail">
            <svg viewBox="0 0 12 12"><rect x="1" y="2.5" width="10" height="7" fill="none" stroke="#fff" stroke-width="1.2"/><path d="M1 2.5 L6 6.5 L11 2.5" fill="none" stroke="#fff" stroke-width="1.2"/></svg>
          </span>
          dale@tallowbrookpainting.net
        </li>
        <li class="contact-item">
          <span class="contact-icon icon-web">
            <svg viewBox="0 0 12 12"><circle cx="6" cy="6" r="4.6" fill="none" stroke="#fff" stroke-width="1.1"/><ellipse cx="6" cy="6" rx="2" ry="4.6" fill="none" stroke="#fff" stroke-width="1"/><path d="M1.4 6 H10.6" stroke="#fff" stroke-width="1"/></svg>
          </span>
          www.tallowbrookpainting.net
        </li>
      </ul>
    </div>
    <div class="color-band">
      <span class="band-green"></span>
      <span class="band-yellow"></span>
      <span class="band-red"></span>
    </div>
  </section>

  <section class="card card-back" aria-label="Business card back">
    <span class="brand-square"></span>
    <span class="wordmark">Tallowbrook Painting</span>
  </section>

</body>
</html>
```